Web design for Money Service Business (uncoded)

We need a very basic website with 5-6 pages. Home page, Services, Transfer(How to use our service), About us, Contact us, FAQ
Our company name is Meridale Exchange. We are a company that deals with currency exchange and international money transfer. We do cash exchange and international money transfers to bank accounts all over the world. We offer highly competitive exchange rates so usually attract customers who transfer money over $10,000. Our niche is with larger sums of money, the design needs to be professional and communicate trust, security and stability.

```html
<!DOCTYPE html>
<html lang="en">
<head>
<meta charset="utf-8">
<title>Meridale Exchange – International Money Transfer</title>
<link rel="stylesheet" href="https://fonts.googleapis.com/css2?family=Questrial&family=Arimo:ital,wght@0,400;0,700;1,400;1,700&display=swap">
<style>
:root{
  --page:#e6e6e6;
  --panel:#ececec;
  --white:#ffffff;
  --navy:#1f4f86;
  --link:#1a7bc4;
  --orange:#f0961e;
  --text:#444444;
  --dark:#222222;
  --rule:#c9c9c9;
  --footer:#1e1e1e;
  --footer-base:#121212;
  --footer-text:#b4b4b4;
  --select:#5f5f5f;
  --sky-top:#25284e;
  --sky-mid:#4a4470;
  --glow-warm:#b88a58;
  --glow-cool:#7fb0e0;
  --water:#2a1f1c;
}
*{margin:0;padding:0;box-sizing:border-box}
html,body{width:956px;height:1200px;overflow:hidden;background:var(--page)}
body{position:relative;font-family:"Arimo",Arial,sans-serif;color:var(--text)}
.abs{position:absolute}
.title{font-family:"Questrial",sans-serif;color:var(--navy);font-weight:400}
.double-rule{position:absolute;left:120px;width:720px;height:3px;border-top:1px solid var(--rule);border-bottom:1px solid var(--white)}

/* header */
.brand{left:122px;top:30px}
.brand-name{font-family:"Questrial",sans-serif;font-size:22px;color:var(--navy);letter-spacing:.3px;line-height:1}
.brand-tag{font-size:7.6px;letter-spacing:2.4px;color:var(--orange);margin-top:4px}
.nav{right:116px;top:38px;display:flex;align-items:center;gap:15px;font-family:"Questrial",sans-serif;font-size:10.5px;color:#333;text-transform:uppercase}
.nav svg{margin-right:14px}

.hero{left:120px;top:86px;width:720px;height:335px;
  background:
    radial-gradient(ellipse 22% 30% at 22% 58%, rgba(255,205,140,.45), transparent 70%),
    radial-gradient(ellipse 16% 38% at 48% 48%, rgba(230,200,150,.35), transparent 70%),
    radial-gradient(ellipse 20% 40% at 72% 45%, rgba(140,190,240,.40), transparent 70%),
    radial-gradient(ellipse 18% 30% at 90% 60%, rgba(240,170,100,.40), transparent 70%),
    radial-gradient(ellipse 50% 10% at 50% 88%, rgba(240,180,110,.35), transparent 70%),
    linear-gradient(180deg,var(--sky-top) 0%,var(--sky-mid) 22%,#6a5878 40%,#7e6458 55%,var(--glow-warm) 70%,#4a3628 79%,#8a6440 86%,var(--water) 94%,#18161a 100%)}

/* welcome */
.welcome-title{left:120px;top:464px;font-size:18.5px}
.welcome-text{left:120px;top:498px;width:353px;font-size:9.5px;line-height:12.1px;text-align:justify}
.portrait{left:493px;top:501px;width:105px;height:92px;background:linear-gradient(160deg,#b9c2c8 0%,#7d868c 45%,#2b2d33 100%)}
.news-side{left:632px;top:464px;width:208px}
.news-side .title{font-size:18.5px;display:flex;align-items:center;gap:8px}
.news-side .title::after{content:"";flex:1;height:1px;background:var(--rule)}
.news-item{font-size:9.2px;line-height:11px}
.news-item:first-of-type{margin-top:11px}
.news-date{color:var(--orange)}
.news-item + .news-item{border-top:1px solid var(--rule);padding-top:8px;margin-top:6px}

/* panels */
.panel{top:685px;width:178px;height:200px;background:var(--panel);box-shadow:0 0 3px rgba(0,0,0,.12)}
.panel.live{background:var(--white)}
.panel-title{position:absolute;left:12px;right:12px;top:18px;font-family:"Questrial",sans-serif;font-size:13px;color:var(--navy);text-transform:uppercase;padding-bottom:6px;border-bottom:1px solid var(--rule)}
.converter{font-size:9.5px;color:var(--dark)}
.field-label{position:absolute;left:12px}
.select{position:absolute;left:12px;width:155px;height:13px;background:var(--select);color:#fff;font-size:7.5px;line-height:13px;padding-left:5px}
.select::after{content:"";position:absolute;right:4px;top:4px;border:4px solid transparent;border-top:5px solid #fff}
.amount{position:absolute;left:12px;top:137px;width:60px;height:13px;background:var(--select);color:#fff;font-size:7.5px;line-height:13px;padding-left:5px}
.result{position:absolute;left:12px;top:164px;font-size:8.5px}
.convert-btn{position:absolute;left:121px;top:161px;width:46px;height:17px;background:var(--navy);color:#fff;font-size:10px;text-align:center;line-height:17px}
.live-lead{position:absolute;left:14px;top:54px;width:155px;font-size:9.5px;line-height:12px;color:var(--dark)}
.chart{position:absolute;left:14px;top:86px}
.live-note{position:absolute;left:14px;top:154px;width:155px;font-size:7.5px;line-height:10.5px;color:var(--dark)}
.panel-news-item{position:absolute;left:12px;width:156px;font-size:9px;line-height:11.5px}
.panel-news-item .date{color:var(--link);font-size:8.5px}
.panel-news-item .head{color:var(--dark);font-size:9.5px}
.panel-news-item a{color:var(--link);text-decoration:none}
.see-all{position:absolute;left:0;bottom:0;width:100%;height:20px;border-top:1px solid #d4d4d4;text-align:center;font-size:9px;line-height:20px;color:var(--dark)}
.quote{position:absolute;left:18px;top:70px;width:145px;font-size:10px;line-height:13.5px;font-style:italic;color:var(--dark)}
.quote-name{position:absolute;left:18px;top:138px;font-size:10px;line-height:12px;font-style:italic;color:var(--dark)}
.quote-name b{color:var(--link)}

/* contact strip */
.contact-strip{left:120px;top:908px;width:720px;height:31px;border-top:1px solid var(--rule);display:flex;align-items:center;font-size:9.5px;color:var(--dark)}
.contact-strip .item{display:flex;align-items:center;gap:8px}
.region{width:178px;height:15px;background:#fff;border:1px solid #ccc;font-size:7px;line-height:13px;padding-left:5px;position:relative}
.region::after{content:"";position:absolute;right:6px;top:4px;border:5px solid transparent;border-top:5px solid #333}
.social{margin-left:auto;display:flex;align-items:center;gap:8px;font-size:10.5px}
.social span.dot{width:11px;height:11px;background:#333;display:inline-block}

/* footer */
.footer{left:120px;top:939px;width:720px;height:237px;background:var(--footer)}
.footer-cols{position:absolute;left:17px;top:20px;display:flex}
.footer-col{font-size:7.5px;line-height:12.8px;color:var(--footer-text)}
.footer-col h4{font-weight:400;font-size:9.5px;color:var(--orange);line-height:12px;margin-bottom:2px}
.disclaimer{position:absolute;left:13px;top:142px;width:697px;font-size:7.6px;line-height:12.8px;color:var(--footer-text);text-align:justify}
.disclaimer span{color:var(--link)}
.footer-base{left:120px;top:1176px;width:720px;height:24px;background:var(--footer-base);display:flex;align-items:center;padding:0 12px;font-size:7.2px;color:var(--footer-text);gap:13px}
.footer-base .copy{margin-left:auto}
</style>
</head>
<body>

<header>
  <div class="abs brand">
    <div class="brand-name">MERIDALE EXCHANGE</div>
    <div class="brand-tag">INTERNATIONAL MONEY TRANSFER</div>
  </div>
  <nav class="abs nav">
    <svg width="13" height="12" viewBox="0 0 13 12" aria-hidden="true"><path d="M6.5 0 13 6h-2v6H8V8H5v4H2V6H0z" fill="#f0961e"/></svg>
    <span>About us</span><span>Services</span><span>Transfer</span><span>Contact us</span>
  </nav>
</header>
<div class="double-rule" style="top:78px"></div>

<div class="abs hero" role="img" aria-label="City skyline at night with illuminated towers reflected in the harbour"></div>

<main>
  <h1 class="abs title welcome-title">Welcome to Meridale Exchange</h1>
  <p class="abs welcome-text">Nam quis ligula a nibh fermentum venenatis vitae nec neque. Etiam non felis mi. Quisque feugiat, lectus non feugiat consectetur, purus ipsum lobortis nisl, a sollicitudin risus arcu elementum risus. Sed feugiat mollis neque. Suspendisse potenti. Sed libero dui, consequat vel ultrices quis, faucibus iaculis nisi. Pellentesque sit amet eleifend augue. Fusce viverra nisl eu magna imperdiet euismod a vel tortor. Donec vulputate pellentesque erat molestie lacinia. Nullam in tincidunt dui. Integer eget ipsum ante, nec venenatis velit. Phasellus metus nisi, feugiat a auctor non, rutrum nec felis. Cras scelerisque gravida ipsum ut convallis.</p>
  <div class="abs portrait" role="img" aria-label="Portrait of a company director in a dark suit"></div>

  <aside class="abs news-side">
    <h2 class="title">News</h2>
    <div class="news-item"><div class="news-date">26.11.2013</div>Aliquam bibendum pretium metus vel ornare. Sed lacinia putate dolor, nec congue nunc accumsan at. Praesent</div>
    <div class="news-item"><div class="news-date">26.11.2013</div>Aliquam bibendum pretium metus vel ornare. Sed lacinia putate dolor, nec congue nunc accumsan at. Praesent</div>
  </aside>
</main>
<div class="double-rule" style="top:647px"></div>

<section class="abs panel converter" style="left:120px">
  <h3 class="panel-title">Currency converter</h3>
  <div class="field-label" style="top:55px">Currency from:</div>
  <div class="select" style="top:68px">GBP - Great British Pound</div>
  <div class="field-label" style="top:87px">Currency to:</div>
  <div class="select" style="top:99px">EUR - Euro</div>
  <div class="field-label" style="top:125px">Amount:</div>
  <div class="amount">1</div>
  <div class="result">= 1.19 EUR( Rate =1.1966 )</div>
  <div class="convert-btn">Convert</div>
</section>

<section class="abs panel live" style="left:300px">
  <h3 class="panel-title">Live rates</h3>
  <p class="live-lead">Aenean dapibus lorem laoreet ante pharetra ornare malesuada orci</p>
  <svg class="chart" width="152" height="58" viewBox="0 0 152 58" role="img" aria-label="Exchange rate line chart">
    <defs><linearGradient id="rateBg" x1="0" y1="0" x2="0" y2="1"><stop offset="0" stop-color="#2f78c8"/><stop offset="1" stop-color="#1a4f94"/></linearGradient></defs>
    <rect width="152" height="58" fill="url(#rateBg)"/>
    <g stroke="#4d92d8" stroke-width=".5"><line x1="0" y1="14" x2="152" y2="14"/><line x1="0" y1="28" x2="152" y2="28"/><line x1="0" y1="42" x2="152" y2="42"/></g>
    <polygon fill="#7fb4ea" opacity=".8" points="0,50 0,36 6,30 10,38 14,26 18,34 22,20 26,32 30,28 34,40 38,24 42,30 46,18 50,34 54,28 58,22 62,36 66,26 70,14 74,30 78,24 82,38 86,20 90,32 94,26 98,12 102,30 106,22 110,34 114,24 118,18 122,32 126,26 130,36 134,20 138,30 142,24 146,34 152,28 152,50"/>
    <rect y="50" width="152" height="8" fill="#163f78"/>
    <g fill="#9cc3ee" font-size="3.5" font-family="Arimo,sans-serif"><text x="28" y="55.5">12 Nov</text><text x="70" y="55.5">19 Nov</text><text x="112" y="55.5">26 Nov</text></g>
  </svg>
  <p class="live-note">Morbi adipiscing sodales condimentum. Nunc porta hendrerit turpis, nec pharetra enim interdum id. Donec vel metus</p>
</section>

<section class="abs panel" style="left:480px">
  <h3 class="panel-title">News</h3>
  <div class="panel-news-item" style="top:55px"><div class="date">Date: 06.11.2013</div><div class="head">Aliquam venenatis risus ac nisi</div>Quisque vitae mi quis metus porttitor porta vitae eget lacus...<a>read more</a></div>
  <div class="panel-news-item" style="top:117px"><div class="date">Date: 06.11.2013</div><div class="head">Aliquam venenatis risus ac nisi</div>Quisque vitae mi quis metus porttitor porta vitae eget lacus...<a>read more</a></div>
  <div class="see-all">See All</div>
</section>

<section class="abs panel" style="left:660px">
  <h3 class="panel-title">Testimonials</h3>
  <p class="quote">“ Aenean dapibus lorem laoreet ante pharetra ornare malesuada ornare. Ut volutpat ipsum ipsum, eget suscipit mauris. ”</p>
  <p class="quote-name"><b>Morbi adipiscing sodales</b><br>Ut volutpat ipsum</p>
</section>

<div class="abs contact-strip">
  <div class="item" style="margin-left:11px">
    <svg width="13" height="9" viewBox="0 0 13 9" aria-hidden="true"><rect width="13" height="9" fill="#555"/><path d="M0 0l6.5 5L13 0" stroke="#e6e6e6" fill="none"/></svg>
    Email: info@meridale-mail.example
  </div>
  <div class="item" style="margin-left:24px">
    <svg width="9" height="12" viewBox="0 0 9 12" aria-hidden="true"><path d="M2 0h2l1 3-1.5 1.2c.6 1.6 1.5 2.8 2.8 3.7L7.6 6.8 9 8.6 8 11c-4.2-.5-7.6-5-7.6-9.4z" fill="#555"/></svg>
    Phone: 000-000-0000
  </div>
  <div class="region" style="margin-left:22px">Select your region</div>
  <div class="social">Follow Us <span class="dot"></span><span class="dot"></span><span class="dot"></span></div>
</div>

<footer class="abs footer">
  <div class="footer-cols">
    <div class="footer-col" style="width:89px"><h4>Personal</h4>Online Transfers<br>Telephone Transfers<br>Regular Transfers<br>Other Services</div>
    <div class="footer-col" style="width:89px"><h4>Personal</h4>Online Transfers<br>Telephone Transfers<br>Regular Transfers<br>Other Services</div>
    <div class="footer-col" style="width:89px"><h4>Business</h4>Online Payments<br>FX Dealing<br>Corporate FXA<br>Other Services</div>
    <div class="footer-col" style="width:99px"><h4>Why Meridale</h4>About Us<br>Customer Mission<br>Behind The Scenes<br>Latest News<br>Regulatory</div>
    <div class="footer-col" style="width:96px"><h4>Marketwatch</h4>Live Exchange Rates<br>Currency Charts<br>Market Briefings</div>
    <div class="footer-col" style="width:72px"><h4>Contact us</h4>Personal<br>Business<br>Careers</div>
    <div class="footer-col" style="width:67px"><h4>Register</h4>Personal<br>Business</div>
    <div class="footer-col"><h4>Manage my account</h4>Log in<br>Forgotten password<br>Get a quote<br>Make a transfer<br>Track a payment<br>Change of address<br>Help</div>
  </div>
  <p class="disclaimer"><span>Disclaimer :</span> Lorem ipsum dolor sit amet, consectetur adipiscing elit. Sed id tempus enim. Etiam eros velit, rutrum in fringilla id, fermentum sit amet nulla. Nullam cursus mi ut lorem commodo eu pharetra elit blandit. Phasellus malesuada, massa et adipiscing tempor, tellus lacus vulputate dui, non commodo mi neque a dui. Praesent enim dolor, iaculis ut molestie vitae, tempus vitae tortor. Vestibulum ante ipsum primis in faucibus orci luctus et ultrices posuere cubilia Curae; Vestibulum ac nibh eget enim sollicitudin tincidunt et ac lorem. Cras eget sollicitudin lectus. In vel turpis lacus, vitae fringilla urna. Etiam et tellus vel turpis cursus egestas ut vel risus. Nunc sapien lorem, pretium a sodales sit amet, dictum id tellus. In ante mauris, laoreet eu tempus eu, egestas nec leo. Nunc condimentum massa vel erat tristique blandit. Donec quis lectus sapien.foreign exchange you should carefully consider your investment objectives, level of experience, and risk appetite. the possibility exists that you could sustain a loss of some or all of your initial investment and therefore you should not invest money that you cannot afford to lose. you should be aware of all the risks associated with foreign exchange trading, and seek advice from an independent financial advisor if you have any doubts.</p>
</footer>
<div class="abs footer-base">
  <span>Privacy Policy</span><span>Disclaimer</span><span>Complaints Charter</span><span>Staying Safe</span><span>Affiliates</span><span>Registration</span><span>Sitemap</span>
  <span class="copy">© Copyright Meridale Exchange 2013.</span>
</div>

</body>
</html>
```